Harlow Ironworks Business Card

We need a business card design for a new small metal fabrication business in rural NSW, Australia.

The business (Harlow Ironworks) is owner operated by a man with the initials KB - much of the branding comes from this name.

Harlow Ironworks designs, engineers, repairs and manufactures a range of custom, quality metal works including vehicle trays, agricultural machinery impliments, trailers, wood splitters, fire pits, furniture etc.

The brand position focuses on custom work of the highest quality.

Business card design should show quality, attention to detail and stand out among a mass of business cards.

Logos are in the files

The grey color may be changed on the logo if required to stand out more.

There is an image attached of a simple card that is liked because it is clean, clear, simple, masculine and effective. It says 'quality'. As most of the work we do is custom it would be good to have the business card speak to this.

Target Market(s)

Rural and regional based Australians. Primarily adult male 25-60 yrs. Primary production / rural / travelling lifestyle.

Industry/Entity Type

Metal Fabrication

Contact Information for Business Card

The words 'custom quality fabrications' would be great somewhere perhaps on the backside (not on the information side)
Name
title
Phone: 0418 539 746 and (02) 6193 4827
email: info@harlowiw.com.au
www.harlowiw.com.au

address (2 lines)

Requirements
Nice to have
• Background colour should be very navy blue or black.
Should not have
• NO orange and blue combinations.
• Navy is OK

```html
<!DOCTYPE html>
<html lang="en">
<head>
<meta charset="utf-8">
<title>Harlow Ironworks – Business Card</title>
<link rel="stylesheet" href="https://fonts.googleapis.com/css2?family=Open+Sans:wght@400;600;700&display=swap">
<style>
  :root {
    --backdrop: #3a3b3d;
    --card: #1d2022;
    --steel: #a7a8a9;
    --steel-soft: #8e9091;
    --green: #5ec23b;
  }
  * { box-sizing: border-box; margin: 0; padding: 0; }
  html, body {
    width: 1200px; height: 1189px; overflow: hidden;
    background: var(--backdrop);
    font-family: "Open Sans", Arial, sans-serif;
  }
  .stage {
    width: 1200px; height: 1189px;
    display: flex; flex-direction: column; align-items: center;
    padding-top: 52px; gap: 56px;
  }
  .card {
    position: relative;
    width: 900px; height: 514px;
    background: var(--card);
    border-radius: 34px;
    box-shadow: 0 14px 30px rgba(0,0,0,.45);
    overflow: hidden;
  }
  .brand {
    display: flex; align-items: center; gap: 22px;
    color: var(--steel); font-weight: 700;
  }
  .brand-square {
    width: 70px; height: 70px; background: var(--green); flex: none;
  }
  .brand-name { font-size: 64px; letter-spacing: 1px; line-height: 1; white-space: nowrap; }

  /* logo side */
  .card--logo { display: flex; flex-direction: column; align-items: center; justify-content: center; }
  .card--logo .website {
    margin-top: 46px; color: var(--steel-soft); font-size: 24px; letter-spacing: 1px;
  }

  /* info side */
  .card--info .brand { position: absolute; left: 64px; top: 74px; }
  .card--info .brand-square { width: 60px; height: 60px; }
  .card--info .brand-name { font-size: 56px; }
  .person {
    position: absolute; right: 70px; top: 196px; text-align: right;
  }
  .person-name { color: var(--steel); font-weight: 700; font-size: 30px; line-height: 1.1; }
  .person-title {
    color: var(--green); font-size: 23px; line-height: 1.2;
    border-bottom: 2px solid var(--green); padding-bottom: 2px; padding-left: 40px;
  }
  .rule {
    position: absolute; left: 64px; right: 70px; top: 300px;
    height: 2px; background: var(--green);
  }
  .address {
    position: absolute; right: 70px; top: 320px; text-align: right;
    color: var(--steel-soft); font-size: 24px; line-height: 1.35;
  }
  .contacts {
    position: absolute; left: 64px; bottom: 42px;
    list-style: none; color: var(--steel); font-size: 27px; line-height: 1;
  }
  .contacts li { display: flex; align-items: center; gap: 14px; margin-top: 10px; }
  .contacts svg { width: 28px; height: 28px; flex: none; }
</style>
</head>
<body>
<main class="stage">
  <section class="card card--logo">
    <div class="brand">
      <span class="brand-square"></span>
      <span class="brand-name">Harlow Ironworks</span>
    </div>
    <p class="website">harlowiw.com.au</p>
  </section>

  <section class="card card--info">
    <div class="brand">
      <span class="brand-square"></span>
      <span class="brand-name">Harlow Ironworks</span>
    </div>
    <div class="person">
      <p class="person-name">Kieran Brody</p>
      <p class="person-title">Director</p>
    </div>
    <div class="rule"></div>
    <p class="address">PO Box 418 Wattle Lane<br>Holbrook NSW 2644</p>
    <ul class="contacts">
      <li>
        <svg viewBox="0 0 28 28" aria-hidden="true"><rect width="28" height="28" rx="4" fill="#5ec23b"/><path d="M6 11c0-3 4-4 8-4s8 1 8 4l-3 1-1-2h-8l-1 2zM9 13h10l2 8H7z" fill="#1d2022"/><circle cx="14" cy="17" r="2" fill="#5ec23b"/></svg>
        <span>(02) 6193 4827</span>
      </li>
      <li>
        <svg viewBox="0 0 28 28" aria-hidden="true"><rect width="28" height="28" rx="4" fill="#5ec23b"/><path d="M6 11c0-3 4-4 8-4s8 1 8 4l-3 1-1-2h-8l-1 2zM9 13h10l2 8H7z" fill="#1d2022"/><circle cx="14" cy="17" r="2" fill="#5ec23b"/></svg>
        <span>0418 539 746</span>
      </li>
      <li>
        <svg viewBox="0 0 28 28" aria-hidden="true"><rect width="28" height="28" rx="4" fill="#5ec23b"/><rect x="5" y="8" width="18" height="13" fill="none" stroke="#1d2022" stroke-width="2"/><path d="M5 8l9 7 9-7" fill="none" stroke="#1d2022" stroke-width="2"/></svg>
        <span>info@harlowiw.com.au</span>
      </li>
    </ul>
  </section>
</main>
</body>
</html>
```